Marlowick community hall home page

We are building a modern, responsive website & booking system for our community hall. For this PixelForge task, we would like to receive design ideas for the home page.
There are no limits on the colours or fonts that can be used. We are looking for a modern, fresh design with a local/community feel. We don’t have a logo but we also recognise that our name is quite long! … So initials (Marlowick Community Hall) instead of the name would be fine.
People book our community hall for a range of activities including: fitness classes, wedding receptions, birthday parties, business meetings, teaching, community events, charity fundraisers and other celebrations.
We have three main goals for the website. The first is that people can check our calendar and make a booking for an available time slot. The second is that they can read about our facilities and the prices for hiring them. The third is that people can find out about upcoming activities & events.
CTA: Book now
A button that links to a booking request form. (The form is not part of this design project)
Primary/Header navigation:
Home | Calendar | Facilities | Prices | Photos | News | Contact
Secondary/Footer navigation:
Chatterleaf | Quillcast
Login | Register | Privacy policy | Terms & conditions
Example texts (lorem ipsum etc. is also fine):
We have everything you need from a venue, whether it’s an elegant room with ample flexible space, a lavish and elegant hall for a wedding reception, a conference room that fits 125 delegates or a easy access venue to the town centre.
The hall is available for hire for wedding receptions, birthday celebrations, anniversaries, children's parties, presentations, lectures, fitness groups, and will comfortably accommodate all your guests.
This venue is well equipped with a modern kitchen, a range of audio and technical services, hearing loop, licensed bar, conference facilities, disabled access and unlimited free WiFi.
You can use this website to find out more about our rooms, equipment and the services we can offer and use the calendar to see where we have rooms available. You can also book rooms using our online booking system.
To the front of the building is a large public open grassed area across which is a row of shops. To the rear of the building is the large car park, including spaces for blue badge holders and a large enclosed cycle rack. This area also has extensive gardens, with seating and planting areas maintained by local volunteers.
The community hall is run and managed by volunteers of the Marlowick Community Organisation. Our objectives are to increase opportunities for people living in and around Pepperton.
We are passionate about being the heart of the community; caring for this community centred property and visitors are at the heart of all we do.
Where to go next
— Check when the hall is free
— Read our booking policy documents
— Make a booking reservation
Amenities
— Free WiFi
— Free car parking
— Fully equipped kitchen
— Hearing loop
Details for our most popular facilities (rooms):
Name: Main hall
Short description: A 127 square metre main hall with entrance lobby, toilets, a well-equipped kitchen and separate storage facilities. Three sets of double doors provide access to a large paved area and the adjacent playing field.
Capacity: 180 people
Price: £10-20 per hour
Links: More info | Book now
Name: Large meeting room
Short description: A delightful, spacious room with an outlook and access to the small walled garden. Ideal for meetings and small gatherings - it has its own access door and the use of a disabled W/C. We offer a reduced rate for this room when booked together with the main hall.
Capacity: 20 people
Price: £6-12 per hour
Attachments:
We have attached some photos of the hall & some (royalty free) stock images for inspiration.

```html
<!DOCTYPE html>
<html lang="en">
<head>
<meta charset="utf-8">
<title>Marlowick Community Hall – Home</title>
<link rel="stylesheet" href="https://fonts.googleapis.com/css2?family=Montserrat:wght@500;600;700;800&family=Open+Sans:wght@400;600;700&display=swap">
<style>
:root{
  --blue:#2b3fb4;
  --blue-dark:#1f2f8c;
  --ink:#1b1d2a;
  --text:#5c6070;
  --muted:#8a8e9c;
  --tint:#eef1fb;
  --footer:#ececef;
  --white:#ffffff;
  --line:#dfe2ea;
}
*{box-sizing:border-box;margin:0;padding:0}
html,body{width:1200px;height:4648px;overflow:hidden}
body{position:relative;background:var(--white);font-family:"Open Sans",Arial,sans-serif;color:var(--text)}
h1,h2,h3,h4{font-family:"Montserrat",Arial,sans-serif;color:var(--ink)}
.site-name{display:flex;align-items:center;gap:10px;font:600 17px "Open Sans",Arial,sans-serif}
.site-name::before{content:"";width:10px;height:10px;border-radius:50%;background:currentColor}
.btn{position:absolute;display:flex;align-items:center;justify-content:center;background:var(--blue);color:var(--white);font:600 15px "Montserrat",Arial,sans-serif;border-radius:6px}
.photo{position:absolute;border-radius:4px}
.eyebrow{position:absolute;font:500 17px "Montserrat",Arial,sans-serif;color:var(--blue);display:flex;align-items:center;gap:18px}
.eyebrow::before{content:"";width:70px;height:2px;background:var(--blue)}
.para{position:absolute;font-size:16px;line-height:26px;color:var(--text)}

/* hero */
.hero{position:absolute;left:0;top:0;width:1200px;height:600px;background:linear-gradient(160deg,#0e1634 0%,#1d2b55 40%,#3a4f7a 62%,#121a36 100%)}
.hero-light{position:absolute;left:640px;top:60px;width:560px;height:460px;background:radial-gradient(ellipse at 60% 45%,rgba(235,214,160,.55),rgba(120,130,170,.15) 55%,transparent 75%)}
.nav{position:absolute;top:18px;left:176px;right:176px;height:36px;display:flex;align-items:center}
.nav .site-name{color:var(--white)}
.nav ul{list-style:none;display:flex;gap:30px;margin-left:auto}
.nav a{color:var(--white);font:500 16px "Montserrat",Arial,sans-serif;text-decoration:none}
.hero-social{position:absolute;left:66px;top:220px;display:flex;flex-direction:column;gap:26px}
.hero-social span{width:16px;height:16px;border-radius:50%;border:2px solid rgba(255,255,255,.85)}
.hero h1{position:absolute;left:176px;top:204px;width:360px;font-size:40px;line-height:48px;color:var(--white);font-weight:700}
.hero .eyebrow{left:176px;top:156px;color:var(--white)}
.hero .eyebrow::before{background:var(--white)}
.hero .para{left:176px;top:312px;width:320px;color:#dfe3f2;font-size:16px;line-height:24px}
.slide-count{position:absolute;right:46px;top:502px;color:var(--white);font:700 22px "Montserrat",Arial,sans-serif}
.slide-count small{font-size:13px;font-weight:500;opacity:.7}

/* booking bar */
.booking{position:absolute;left:288px;top:552px;width:616px;height:96px;background:var(--white);border-radius:4px;box-shadow:0 10px 30px rgba(20,30,70,.15);display:flex;align-items:center;padding:0 28px 0 40px;gap:50px}
.field b{display:block;font:700 15px "Montserrat",Arial,sans-serif;color:var(--ink);margin-bottom:6px}
.field span{font-size:13px;color:var(--muted)}
.booking .btn{position:static;margin-left:auto;width:116px;height:50px}

/* about */
.about h2{position:absolute;left:680px;top:776px;width:340px;font-size:40px;line-height:48px;font-weight:700}

/* facilities */
.facilities{position:absolute;left:0;top:1264px;width:1200px;height:796px;background:var(--tint)}
.center-eyebrow{position:absolute;left:0;width:1200px;text-align:center;font:500 18px "Montserrat",Arial,sans-serif;color:var(--blue)}
.center-title{position:absolute;left:0;width:1200px;text-align:center;font-size:40px;font-weight:700}
.room{position:absolute;top:200px;width:410px}
.room .photo{position:relative;width:410px;height:224px;border-radius:6px}
.room-head{display:flex;align-items:baseline;margin-top:22px}
.room h3{font-size:21px;font-weight:700}
.price{margin-left:auto;font:700 16px "Montserrat",Arial,sans-serif;color:var(--ink)}
.price small{font-weight:500;font-size:12px;color:var(--muted)}
.room p{margin-top:10px;font-size:13px;line-height:20px;color:var(--text);width:300px}
.amenities{display:flex;gap:26px;margin-top:22px}
.amenity{width:76px;text-align:center;font-size:12px;line-height:16px;color:var(--text)}
.amenity svg{display:block;margin:0 auto 8px}
.arrow{position:absolute;width:32px;height:32px;border-radius:50%;background:var(--blue);display:flex;align-items:center;justify-content:center}

/* testimonial */
.dots{position:absolute;left:480px;top:2084px;width:80px;height:70px;background-image:radial-gradient(circle,#c5cbe6 2px,transparent 2.5px);background-size:12px 12px}
.testimonial h2{position:absolute;left:608px;top:2180px;font-size:36px;font-weight:700}
.author{position:absolute;left:608px;top:2380px;font:700 21px "Montserrat",Arial,sans-serif;color:var(--ink)}
.role{position:absolute;left:608px;top:2414px;font-size:13px;color:var(--muted)}
.avatar{position:absolute;left:608px;top:2448px;width:62px;height:62px;border-radius:50%;background:linear-gradient(135deg,#c96b55,#3f2a2f)}
.slide-dots{position:absolute;display:flex;gap:10px}
.slide-dots span{width:6px;height:6px;border-radius:50%;background:#b6bac7}
.slide-dots span.on{background:var(--ink)}

/* gallery */
.gallery{position:absolute;left:0;top:2600px;width:1200px;height:832px;background:var(--tint)}
.gallery h2{position:absolute;left:176px;top:122px;width:220px;font-size:32px;line-height:40px;font-weight:700}

/* articles */
.article{position:absolute;top:3668px;width:262px}
.article .photo{position:relative;width:262px;height:172px}
.date{margin-top:30px;font-size:12px;color:var(--blue)}
.article h4{margin-top:10px;font-size:15px;line-height:21px;font-weight:600}
.article p{margin-top:10px;font-size:13px;line-height:19px;color:var(--text)}
.article a{display:block;margin-top:18px;font:700 15px "Montserrat",Arial,sans-serif;color:var(--blue);text-decoration:none}

/* footer */
.footer{position:absolute;left:0;top:4200px;width:1200px;height:448px;background:var(--footer)}
.footer .site-name{position:absolute;left:184px;top:68px;color:var(--ink)}
.footer-about{position:absolute;left:184px;top:118px;width:200px;font-size:13px;line-height:20px}
.footer-social{position:absolute;left:184px;top:226px;display:flex;gap:18px}
.footer-social span{width:14px;height:14px;border-radius:50%;background:var(--ink)}
.fcol{position:absolute;top:68px}
.fcol h4{font-size:16px;font-weight:700;margin-bottom:22px}
.fcol ul{list-style:none}
.fcol li{font-size:13px;line-height:27px;color:var(--ink)}
.contact-row{display:flex;align-items:center;gap:12px;font-size:13px;color:var(--ink);margin-bottom:16px}
.footer-line{position:absolute;left:176px;width:848px;top:332px;height:1px;background:#cfd2da}
.copyright{position:absolute;left:0;width:1200px;top:364px;text-align:center;font-size:12px;color:var(--text)}
</style>
</head>
<body>

<!-- Hero -->
<header class="hero">
  <div class="hero-light" role="img" aria-label="Community hall building lit up at night beside the water"></div>
  <nav class="nav">
    <span class="site-name">Marlowick Community Hall</span>
    <ul>
      <li><a>Home</a></li><li><a>Calendar</a></li><li><a>Facilities</a></li><li><a>Prices</a></li><li><a>Photos</a></li><li><a>News</a></li><li><a>Contact</a></li>
    </ul>
  </nav>
  <div class="hero-social" aria-label="Social links"><span></span><span></span><span></span><span></span><span></span></div>
  <div class="eyebrow">Welcome</div>
  <h1>Online Booking For Your Hall.</h1>
  <p class="para">Lorem ipsum dolor sit amet consectetur adipiscing elit sed do.</p>
  <div class="btn" style="left:176px;top:396px;width:112px;height:48px">Book Now!</div>
  <div class="slide-count">01<small>/05</small></div>
</header>

<div class="booking">
  <div class="field"><b>Guests</b><span>50+</span></div>
  <div class="field"><b>Booking Type</b><span>Anniversaries</span></div>
  <div class="field"><b>Event Date</b><span>12/07/2021</span></div>
  <div class="btn">Search</div>
</div>

<!-- About -->
<section class="about">
  <div class="photo" style="left:176px;top:722px;width:264px;height:186px;background:linear-gradient(160deg,#d9d4cf,#7d8fb8 60%,#2c3b7a)" role="img" aria-label="Fitness class with mats in the hall"></div>
  <div class="photo" style="left:452px;top:722px;width:188px;height:350px;background:linear-gradient(170deg,#3f5b35,#e7d4d6 45%,#c9a1a8 70%,#5e6b44)" role="img" aria-label="Floral wedding table decoration"></div>
  <div class="photo" style="left:228px;top:920px;width:212px;height:268px;background:linear-gradient(170deg,#2a1846,#7b3f8f 45%,#d88a3a 75%,#2b1a3a)" role="img" aria-label="Party room with purple lighting"></div>
  <div class="eyebrow" style="left:680px;top:728px">About us</div>
  <h2>Discover Our Community Hall</h2>
  <p class="para" style="left:680px;top:884px;width:340px;font-size:15px;line-height:24px">Lorem ipsum dolor sit amet, consectetur adipiscing elit, sed do eiusmod tempor incididunt ut labore et dolore magna aliqua. Ut enim ad minim veniam, quis nostrud exercitation ullamco laboris nisi ut aliquip ex ea commodo consequat. Duis aute irure dolor in reprehenderit in voluptate velit esse cillum dolore eu fugiat nulla pariatur. Excepteur sint occaecat.</p>
  <div class="btn" style="left:680px;top:1128px;width:136px;height:52px">Read More</div>
</section>

<!-- Facilities -->
<section class="facilities">
  <div class="center-eyebrow" style="top:66px">Most Popular</div>
  <h2 class="center-title" style="top:104px">Our Facilities</h2>
  <div class="arrow" style="left:120px;top:292px"><svg width="12" height="12" viewBox="0 0 12 12"><path d="M8 2 4 6l4 4" fill="none" stroke="#fff" stroke-width="2"/></svg></div>
  <div class="arrow" style="left:1040px;top:292px"><svg width="12" height="12" viewBox="0 0 12 12"><path d="M4 2l4 4-4 4" fill="none" stroke="#fff" stroke-width="2"/></svg></div>

  <article class="room" style="left:176px">
    <div class="photo" style="background:linear-gradient(180deg,#3a3550,#4e5fa8 45%,#d9dce8)" role="img" aria-label="Main hall set with round tables and chandeliers"></div>
    <div class="room-head"><h3>Main Community Hall</h3><span class="price">£10-20<small>/hour</small></span></div>
    <p>A 127 square metre main hall with entrance lobby, toilets, a well-equipped kitchen...</p>
    <div class="amenities">
      <div class="amenity"><svg width="24" height="20" viewBox="0 0 24 20" fill="none" stroke="#2b3fb4" stroke-width="2"><path d="M2 7a14 14 0 0 1 20 0M5 10.5a9 9 0 0 1 14 0M8.5 14a4 4 0 0 1 7 0"/><circle cx="12" cy="17.5" r="1.2" fill="#2b3fb4"/></svg>Free WiFi</div>
      <div class="amenity"><svg width="22" height="22" viewBox="0 0 22 22" fill="none" stroke="#2b3fb4" stroke-width="2"><rect x="2" y="2" width="18" height="18" rx="3"/><path d="M8 16V6h4a3 3 0 0 1 0 6H8"/></svg>Free car parking</div>
      <div class="amenity"><svg width="22" height="22" viewBox="0 0 22 22" fill="none" stroke="#2b3fb4" stroke-width="2"><rect x="3" y="3" width="16" height="17" rx="2"/><path d="M3 9h16M7 6h2"/></svg>Fully equipped kitchen</div>
      <div class="amenity"><svg width="22" height="22" viewBox="0 0 22 22" fill="none" stroke="#2b3fb4" stroke-width="2"><path d="M6 9a5 5 0 0 1 10 0c0 4-4 4-4 8a3 3 0 0 1-5 1"/><path d="M9 9a2 2 0 0 1 4 0"/></svg>Hearing loop</div>
    </div>
  </article>

  <article class="room" style="left:606px">
    <div class="photo" style="background:linear-gradient(180deg,#d8d6d0,#b7b3a8 50%,#6e6a64)" role="img" aria-label="Large meeting room with tables and a projector screen"></div>
    <div class="room-head"><h3>Large Meeting Room</h3><span class="price">£6-12<small>/hour</small></span></div>
    <p>A delightful, spacious room with an outlook and access to the small walled garden...</p>
    <div class="amenities">
      <div class="amenity"><svg width="24" height="20" viewBox="0 0 24 20" fill="none" stroke="#2b3fb4" stroke-width="2"><path d="M2 7a14 14 0 0 1 20 0M5 10.5a9 9 0 0 1 14 0M8.5 14a4 4 0 0 1 7 0"/><circle cx="12" cy="17.5" r="1.2" fill="#2b3fb4"/></svg>Free WiFi</div>
      <div class="amenity"><svg width="22" height="22" viewBox="0 0 22 22" fill="none" stroke="#2b3fb4" stroke-width="2"><rect x="2" y="2" width="18" height="18" rx="3"/><path d="M8 16V6h4a3 3 0 0 1 0 6H8"/></svg>Free car parking</div>
      <div class="amenity"><svg width="22" height="22" viewBox="0 0 22 22" fill="none" stroke="#2b3fb4" stroke-width="2"><rect x="3" y="3" width="16" height="17" rx="2"/><path d="M3 9h16M7 6h2"/></svg>Fully equipped kitchen</div>
      <div class="amenity"><svg width="22" height="22" viewBox="0 0 22 22" fill="none" stroke="#2b3fb4" stroke-width="2"><path d="M6 9a5 5 0 0 1 10 0c0 4-4 4-4 8a3 3 0 0 1-5 1"/><path d="M9 9a2 2 0 0 1 4 0"/></svg>Hearing loop</div>
    </div>
  </article>

  <div class="btn" style="left:512px;top:652px;width:176px;height:60px">Explore More</div>
</section>

<!-- Testimonial -->
<section class="testimonial">
  <div class="dots"></div>
  <div class="photo" style="left:176px;top:2136px;width:352px;height:384px;background:linear-gradient(180deg,#5a6fb0,#a9c2e8 35%,#c98a5a 65%,#2c2430)" role="img" aria-label="Crowd enjoying a celebration event in the hall"></div>
  <div class="slide-dots" style="left:484px;top:2504px"><span class="on"></span><span></span></div>
  <div class="eyebrow" style="left:608px;top:2140px">Clients Love</div>
  <h2>Love From Our Clients</h2>
  <p class="para" style="left:608px;top:2232px;width:410px;font-size:15px;line-height:24px">Highly recommend consectetur adipiscing elit, sed do eiusmod tempor incididunt ut labore et dolore magna aliqua. Ut enim ad minim veniam, quis nostrud exercitation ullamco laboris nisi ut aliquip ex ea commodo consequat. Duis aute irure dolor in reprehenderit.</p>
  <div class="author">John Doe</div>
  <div class="role">HR Manager</div>
  <div class="avatar" role="img" aria-label="Client portrait"></div>
</section>

<!-- Gallery -->
<section class="gallery">
  <div class="eyebrow" style="left:176px;top:84px">Gallery</div>
  <h2>Explore Our Gallery</h2>
  <p class="para" style="left:176px;top:210px;width:224px;font-size:13px;line-height:20px">Lorem ipsum dolor sit amet consectetur adipiscing elit sed do eiusmod tempor incididunt ut labore et dolore magna aliqua enim.</p>
  <div class="btn" style="left:176px;top:332px;width:104px;height:40px;font-size:12px">View Gallery</div>
  <div class="photo" style="left:500px;top:84px;width:244px;height:220px;background:linear-gradient(135deg,#2d5a7a,#c45a3a 40%,#e3c27a 60%,#3a6a4f)" role="img" aria-label="Stained glass window"></div>
  <div class="photo" style="left:780px;top:212px;width:232px;height:344px;background:linear-gradient(180deg,#6a5a4a,#d8c9b0 50%,#f2ece2)" role="img" aria-label="Candles and wedding table setting"></div>
  <div class="photo" style="left:452px;top:332px;width:304px;height:220px;background:linear-gradient(180deg,#5a4a3a,#8fa3c8 45%,#e6e6ee)" role="img" aria-label="Banquet hall with chandeliers"></div>
  <div class="photo" style="left:176px;top:416px;width:256px;height:184px;background:linear-gradient(160deg,#c8b8a8,#8a6d55 60%,#4a3a30)" role="img" aria-label="Long dining table set for guests"></div>
  <div class="photo" style="left:184px;top:620px;width:264px;height:164px;background:linear-gradient(180deg,#3a2a55,#7a5ab0 50%,#2a2040)" role="img" aria-label="Event hall lit in purple"></div>
  <div class="photo" style="left:468px;top:576px;width:244px;height:208px;background:linear-gradient(180deg,#e2dad0,#a89a8a 55%,#5a4a40)" role="img" aria-label="Reception room with draped chairs"></div>
  <div class="photo" style="left:732px;top:572px;width:280px;height:168px;background:linear-gradient(160deg,#5a8ab0,#d8a0a8 50%,#e8d0b0)" role="img" aria-label="Decorated dessert table"></div>
</section>

<!-- Articles -->
<section class="articles">
  <h2 class="center-title" style="top:3520px;font-size:36px">Our Recent Articles</h2>
  <p class="para" style="left:380px;top:3580px;width:440px;text-align:center;font-size:15px;line-height:22px">Lorem ipsum dolor sit amet, consectetur adipiscing elit, sed do eiusmod tempor incididunt ut labore et dolore.</p>
  <div class="arrow" style="left:108px;top:3862px;background:var(--white);border:1px solid var(--line)"><svg width="12" height="12" viewBox="0 0 12 12"><path d="M8 2 4 6l4 4" fill="none" stroke="#1b1d2a" stroke-width="2"/></svg></div>
  <div class="arrow" style="left:1056px;top:3862px"><svg width="12" height="12" viewBox="0 0 12 12"><path d="M4 2l4 4-4 4" fill="none" stroke="#fff" stroke-width="2"/></svg></div>

  <article class="article" style="left:176px">
    <div class="photo" style="background:linear-gradient(180deg,#7aa6d8,#e0b040 55%,#c07030)" role="img" aria-label="Child playing on a bouncy castle"></div>
    <div class="date">Date : 12/02/2021</div>
    <h4>Lorem ipsum dolor sit amet consectetur aliquam quaerat.</h4>
    <p>Lorem ipsum dolor sit amet, consectetur adipiscing elit sed do.</p>
    <a>Read More</a>
  </article>
  <article class="article" style="left:468px">
    <div class="photo" style="background:linear-gradient(160deg,#efe6da,#d8b890 55%,#a8805a)" role="img" aria-label="Hands preparing baking dough"></div>
    <div class="date">Date : 12/02/2021</div>
    <h4>Lorem ipsum dolor sit amet consectetur aliquam quaerat.</h4>
    <p>Lorem ipsum dolor sit amet, consectetur adipiscing elit sed do.</p>
    <a>Read More</a>
  </article>
  <article class="article" style="left:752px">
    <div class="photo" style="background:linear-gradient(160deg,#f2f0ec,#d8d0c8 55%,#8a9ab8)" role="img" aria-label="Person stretching during a yoga class"></div>
    <div class="date">Date : 12/02/2021</div>
    <h4>Lorem ipsum dolor sit amet consectetur aliquam quaerat.</h4>
    <p>Lorem ipsum dolor sit amet, consectetur adipiscing elit sed do.</p>
    <a>Read More</a>
  </article>
  <div class="slide-dots" style="left:576px;top:4110px"><span class="on"></span><span></span><span></span><span></span></div>
</section>

<!-- Footer -->
<footer class="footer">
  <span class="site-name">Marlowick Community Hall</span>
  <p class="footer-about">Lorem ipsum dolor sit amet, consectetur adipiscing elit, sed do eiusmod tempor incididunt ut labore.</p>
  <div class="footer-social" aria-label="Chatterleaf, Quillcast and other social links"><span></span><span></span><span></span><span></span></div>

  <div class="fcol" style="left:540px">
    <h4>Quick Links</h4>
    <ul><li>Home</li><li>Calendar</li><li>Facilities</li><li>Prices</li><li>Photos</li><li>News</li><li>Contact</li></ul>
  </div>
  <div class="fcol" style="left:696px">
    <h4>Help</h4>
    <ul><li>Login</li><li>Register</li><li>Privacy policy</li><li>Terms &amp; conditions</li></ul>
  </div>
  <div class="fcol" style="left:864px">
    <h4>Contact Us</h4>
    <p style="font-size:13px;line-height:20px;width:170px;margin-bottom:18px">Lorem ipsum dolor sit amet consectetur.</p>
    <div class="contact-row"><svg width="14" height="14" viewBox="0 0 14 14"><path d="M3 1l2.5 3-1.5 1.5a8 8 0 0 0 4.5 4.5L10 8.5l3 2.5-1.5 2C6 13 1 8 1 2.5z" fill="#1b1d2a"/></svg>0123 555 018</div>
    <div class="contact-row"><svg width="14" height="12" viewBox="0 0 14 12"><rect x="1" y="1" width="12" height="10" rx="1" fill="none" stroke="#1b1d2a" stroke-width="1.5"/><path d="M1 2l6 5 6-5" fill="none" stroke="#1b1d2a" stroke-width="1.5"/></svg>info@marlowickhall.org</div>
  </div>

  <div class="footer-line"></div>
  <p class="copyright">Copyright © 2021 All rights reserved</p>
</footer>

</body>
</html>
```